Heath Weight Loss Retreat Website

The brief:
PineLoop is a provider of health & weight loss retreats and wish to redesign their main website. The website needs to provide detailed information about the company’s services whilst gathering the maximum number of leads possible. The website does not aim to get clients to ‘book now’ but to request further information, or ask a question generating a lead/opportunity for the business.

Primary objectives of website
• Gather leads for products (not necessarily to book at that point, but to ‘request more info’)
• Provide detailed information about the health and fitness programs on offer

Demographic Considerations
• Target age group: 30-50
• Predominant client base are female but website should be gender neutral due to some men attending

Design considerations
• Essentially selling ‘travel experiences’ and ‘life transformations’ so needs to be lots of images to display (similar to a hotel website for example)
• Images need to display real people – i.e. larger people, rather than super thin
• Not too much use of flash
• SEO friendly (we have good rankings at present)
• Will be implemented into Joomla, so please consider this on the design
• Colours should be ‘warm’ and ‘friendly’ and gender neutral

Project Requirements & Expectations
Please supply your design ideas with:
• At least 1 (preferably more) homepage examples
• At least 1 (preferably more) internal page examples
Once a preferred design has been selected the following will be produced, tweaked and approved:
• Homepage + 1 internal landing page + 1 internal main page + 1 contact page + 1 info request page

Attachments
We have attached both a homepage and internal page example which demonstates the type of content needed and the calls to action. This is for demonstration purposes only so please ignore colours, fonts, etc and provide your best designs based on a general layout as per attached.

Images:
A selection of example images has been attached. For the homepage images of the retreats themselves should be used alongside images of ‘larger people’.

Further information:
Please contact Simon Thackery at simon.thackery@coralbeaconfiles.com.au

Target Market(s)

Overweight females aged 30-50 are the main target market. However must be gender neutral due to some men using product.

Industry/Entity Type

Weight

Requirements
Should not have
• Not too much flash

```html
<!DOCTYPE html>
<html lang="en">
<head>
<meta charset="utf-8">
<title>PineLoop – Health &amp; Weight Loss Retreats</title>
<link href="https://fonts.googleapis.com/css2?family=Arimo:wght@400;700&family=Tinos:ital,wght@0,700;1,700&display=swap" rel="stylesheet">
<style>
:root{
  --green:#5c9a1b;
  --green-dark:#3f7410;
  --green-light:#eaf3d9;
  --green-pale:#f4f9ec;
  --orange:#e8771c;
  --orange-dark:#c75f0d;
  --text:#4a4a4a;
  --muted:#7a7a7a;
  --line:#d9e3c8;
  --bg:#ffffff;
  --footer:#f2f6ea;
  --photo-sky:#8fb7cf;
  --photo-green:#6f9a4a;
  --photo-warm:#c9a27b;
}
*{box-sizing:border-box;margin:0;padding:0}
html,body{width:876px;height:1200px;overflow:hidden;background:var(--bg)}
body{position:relative;font-family:"Arimo",Arial,sans-serif;color:var(--text);font-size:7px;line-height:1.45}
ul{list-style:none}
.abs{position:absolute}

/* header */
.site-header{left:0;top:0;width:876px;height:88px;border-bottom:3px solid var(--green)}
.brand{left:22px;top:14px;display:flex;align-items:center;gap:6px}
.brand-dot{width:22px;height:22px;border-radius:50%;background:var(--green)}
.brand-name{font-size:22px;font-weight:700;color:var(--green)}
.brand-tag{left:22px;top:42px;font-size:7px;color:var(--muted)}
.nav-col{top:12px;width:118px}
.nav-col h4{font-size:7.5px;color:var(--orange);margin-bottom:3px}
.nav-col li{font-size:6.5px;color:var(--text)}
.nav-col li::before{content:"• ";color:var(--green)}
.header-contact{left:720px;top:12px;width:136px;height:58px;background:var(--green-light);border-radius:4px;padding:6px}
.header-contact .phone{font-size:10px;font-weight:700;color:var(--green-dark)}
.header-contact .small{font-size:6px;color:var(--muted)}
.header-badge{left:832px;top:46px;width:18px;height:18px;background:var(--green)}

/* hero */
.hero{left:0;top:91px;width:876px;height:132px;background:linear-gradient(180deg,var(--photo-sky) 0%,#a9c9b6 45%,var(--photo-green) 100%)}
.hero-box{left:600px;top:102px;width:250px;height:108px;background:rgba(92,154,27,.92);border-radius:6px;padding:10px 12px;color:#fff}
.hero-box h2{font-size:10.5px}
.hero-box p{font-size:6.5px;margin-top:4px}
.btn{display:inline-block;border-radius:4px;color:#fff;font-weight:700;text-align:center}
.btn-orange{background:var(--orange)}
.btn-green{background:var(--green)}
.hero-box .btn{position:absolute;left:58px;bottom:10px;width:180px;padding:6px 0;font-size:8px}

/* left column */
.intro{left:20px;top:232px;width:264px}
.intro .lead{font-size:6.5px;color:var(--muted)}
.intro h1{font-family:"Tinos",Georgia,serif;font-size:21px;line-height:1.15;color:var(--green-dark);margin-top:6px}
.cta-row{left:20px;top:318px;width:264px;display:flex;gap:6px}
.cta-row .btn{font-size:7px;padding:6px 0}
.facts{left:20px;top:344px;width:264px;display:flex;gap:10px;font-size:6.5px}
.facts li::before{content:"• ";color:var(--orange)}
.copy{width:264px;left:20px;font-size:6.5px;color:var(--text)}
.copy p{margin-bottom:6px}
.copy b{color:var(--orange)}
.photo{background:linear-gradient(135deg,var(--photo-warm),var(--photo-green));border-radius:3px}

/* middle column */
.programs{left:292px;top:230px;width:240px;border:1px solid var(--line);border-radius:5px;overflow:hidden}
.programs-head{background:var(--green);color:#fff;text-align:center;padding:6px 0}
.programs-head h3{font-size:10px}
.programs-head span{font-size:6px}
.program{padding:6px 10px;border-bottom:1px solid var(--line);background:var(--green-pale)}
.program h4{font-size:7.5px;color:var(--orange)}
.program ul{display:flex;gap:10px;margin-top:2px;font-size:6.5px}
.program li::before{content:"▸ ";color:var(--green)}
.program-cta{background:var(--green-light);padding:9px 10px;font-size:7px}
.program-cta .btn{margin-top:5px;width:100%;padding:5px 0;font-size:7.5px}

/* right column */
.locations{left:542px;top:230px;width:314px;border:1px solid var(--line);border-radius:5px;overflow:hidden}
.locations-head{background:var(--green);color:#fff;padding:6px 10px;font-size:10px;font-weight:700;text-align:center}
.location{padding:6px 10px;display:flex;gap:8px;border-bottom:1px solid var(--line)}
.location .photo{width:150px;height:62px;flex:none}
.location h4{font-size:8px;color:var(--green-dark)}
.location li{font-size:6.5px}
.location li::before{content:"• ";color:var(--orange)}
.questions{left:542px;top:412px;width:314px;height:96px;background:var(--green-light);border-radius:5px;padding:8px 10px}
.questions h3{font-size:10px;color:var(--green-dark)}
.questions p{font-size:6.5px}
.field{height:11px;background:#fff;border:1px solid var(--line);margin-top:4px;width:190px}
.questions .btn{position:absolute;right:10px;bottom:10px;padding:5px 14px;font-size:7.5px}
.quote{left:542px;top:516px;width:314px;height:92px}
.quote-circle{left:0;top:0;width:118px;height:92px;background:var(--green);border-radius:46px;color:#fff;padding:14px 14px;font-family:"Tinos",Georgia,serif;font-size:11px;font-weight:700;line-height:1.2}
.quote-circle small{display:block;font-family:"Arimo",Arial,sans-serif;font-size:6px;font-weight:400;margin-top:4px}
.quote .photo{left:126px;top:4px;width:188px;height:84px}
.real{left:542px;top:616px;width:314px}
.real h3{font-size:10px;color:var(--green-dark)}
.real .row{display:flex;gap:8px;margin-top:4px}
.real .photo{width:110px;height:62px;flex:none}
.real li{font-size:6.5px}
.real li::before{content:"• ";color:var(--orange)}

/* results */
.results{left:292px;top:930px;width:564px;height:86px;border:1px solid var(--line);border-radius:5px;background:var(--green-pale);padding:8px 12px}
.results h3{font-size:10px;color:var(--green-dark);margin-bottom:4px}
.results .cols{display:flex;gap:12px}
.results ul{flex:1;font-size:6.5px}
.results li::before{content:"✓ ";color:var(--green)}

/* footer */
.site-footer{left:0;top:1026px;width:876px;height:144px;background:var(--footer);border-top:3px solid var(--green);padding:12px 20px;display:flex;gap:14px}
.site-footer .fcol{flex:1}
.site-footer h4{font-size:7.5px;color:var(--green-dark);margin-bottom:4px}
.site-footer li{font-size:6.5px}
.site-footer li::before{content:"• ";color:var(--orange)}
.footer-bar{left:0;top:1170px;width:876px;height:30px;background:var(--green);color:#fff;font-size:6.5px;padding:10px 20px;display:flex;justify-content:space-between}
</style>
</head>
<body>

<header class="site-header abs">
  <div class="brand abs"><span class="brand-dot"></span><span class="brand-name">PineLoop</span></div>
  <div class="brand-tag abs">Health &amp; weight loss retreats</div>

  <nav class="nav-col abs" style="left:250px">
    <h4>The Best Programs</h4>
    <ul><li>Weight Loss Retreat</li><li>Renowned Boot Camp</li><li>Fitness Camp</li><li>At home program</li><li>Local group programs</li></ul>
  </nav>
  <nav class="nav-col abs" style="left:375px">
    <h4>Our Best Locations</h4>
    <ul><li>Blue Mountains</li><li>Sunshine Coast</li><li>Hunter Valley</li><li>Local Programs</li></ul>
  </nav>
  <nav class="nav-col abs" style="left:500px">
    <h4>Success Led by Results</h4>
    <ul><li>Why choose PineLoop</li><li>Expert Team</li><li>Our Research</li><li>Testimonials</li></ul>
  </nav>

  <div class="header-contact abs">
    <div class="small">Call us for free information</div>
    <div class="phone">1300 555 018</div>
    <div class="small">Mon – Fri, 8am – 6pm</div>
  </div>
  <div class="header-badge abs"></div>
</header>

<div class="hero abs" role="img" aria-label="Retreat guests walking together outdoors in green hills"></div>
<div class="hero-box abs">
  <h2>Amazing weight loss &amp; fitness results</h2>
  <p>Join hundreds of real people who changed their lives at our retreats in calm, scenic settings.</p>
  <p>Fun filled facilities, expert team and lasting habits.</p>
  <span class="btn btn-orange">Request more information »</span>
</div>

<section class="intro abs">
  <p class="lead">The PineLoop program works as seen in real lives across the country.</p>
  <h1>“The best weight loss experience of my life”</h1>
</section>

<div class="cta-row abs">
  <span class="btn btn-orange" style="flex:1.4">Request a FREE information pack</span>
  <span class="btn btn-green" style="flex:1">Book your retreat</span>
</div>

<ul class="facts abs">
  <li>Amazing Locations<br>• Expert Team<br>• Proven results</li>
  <li>For all shapes &amp; sizes<br>• Lasting change<br>• Friendly support</li>
</ul>

<div class="copy abs" style="top:384px">
  <p>Hundreds of people have already transformed their lives with PineLoop's proven programs. With PineLoop you will lose weight, lose centimetres, gain fitness and experience healthy living and lifestyle habits.</p>
  <p>Our <b>Weight Loss Retreat</b> program is suitable for people of all ages, shapes, sizes and fitness levels. It is a program fun and extremely effective with amazing weight loss and fitness results. Whether you need a kick start or are planning for a long term change, the program will guide you every step.</p>
</div>
<div class="photo abs" style="left:200px;top:470px;width:84px;height:58px" role="img" aria-label="Guests enjoying a fitness class outdoors"></div>
<div class="copy abs" style="top:470px;width:172px">
  <p>Enjoy a week of nourishing meals, outdoor activities and relaxing treatments in a warm and supportive setting.</p>
  <p>Our team is with you through every session, and the plan goes home with you.</p>
</div>
<div class="copy abs" style="top:540px">
  <p>PineLoop programs are delivered by caring trainers, dietitians and health coaches who understand the challenges of real people. Each day combines movement, education and rest so that results last long after you leave.</p>
  <p>Our <b>Renowned Boot Camp</b> suits those wanting a stronger push, while our <b>At Home</b> program keeps you on track between visits with weekly check ins and simple meal guides.</p>
  <p>Whatever your starting point, you will be surrounded by others on the same journey, with laughter, support and friendships that carry on well beyond the retreat.</p>
</div>
<div class="photo abs" style="left:20px;top:668px;width:264px;height:96px" role="img" aria-label="Healthy fresh meal and fruit on a table"></div>
<div class="copy abs" style="top:774px">
  <p>Our <b>Weight Loss Retreat</b> program is suitable for people of all ages, shapes, sizes and fitness levels. Whether you are brand new to exercise or returning, our team will tailor every session to suit you.</p>
  <p>Request your free information pack today and see how a single week can change the way you feel, move and live.</p>
</div>
<div class="photo abs" style="left:20px;top:852px;width:264px;height:164px" role="img" aria-label="Happy retreat guests together after a hike"></div>

<section class="programs abs">
  <div class="programs-head"><h3>The Best Programs</h3><span>Book now »</span></div>
  <div class="program"><h4>Lose weight with our weight loss retreat</h4><ul><li>Program details</li><li>FREE brochure</li></ul></div>
  <div class="program"><h4>Kick start your health &amp; fitness</h4><ul><li>Program details</li><li>FREE brochure</li></ul></div>
  <div class="program"><h4>Get results at our renowned boot camp</h4><ul><li>Program details</li><li>FREE brochure</li></ul></div>
  <div class="program"><h4>Do it yourself with our home pack</h4><ul><li>Program details</li><li>FREE brochure</li></ul></div>
  <div class="program"><h4>Do it yourself with our local groups</h4><ul><li>Program details</li><li>FREE brochure</li></ul></div>
  <div class="program"><h4>Stay fun and keep on track</h4><ul><li>Program details</li><li>FREE brochure</li></ul></div>
  <div class="program"><h4>Live a fitter healthier lifestyle</h4><ul><li>Program details</li><li>FREE brochure</li></ul></div>
  <div class="program"><h4>Find an approved kid track trainer</h4><ul><li>Program details</li><li>FREE brochure</li></ul></div>
  <div class="program-cta">Not sure which program is right for you? Ask our friendly team for advice.<span class="btn btn-orange">Request information »</span></div>
</section>

<section class="locations abs">
  <div class="locations-head">The best locations &amp; fun filled facilities</div>
  <div class="location">
    <div class="photo" role="img" aria-label="Mountain retreat lodge among trees"></div>
    <div><h4>Blue Mountains</h4><ul><li>Mountain trails</li><li>Heated pool</li><li>Day spa</li><li>Cosy lodge</li></ul></div>
  </div>
  <div class="location">
    <div class="photo" role="img" aria-label="Coastal retreat beside the beach"></div>
    <div><h4>Sunshine Coast</h4><ul><li>Beach walks</li><li>Ocean views</li><li>Yoga deck</li><li>Fresh dining</li></ul></div>
  </div>
</section>

<section class="questions abs">
  <h3>Got Questions?</h3>
  <p>Ask us anything and our team will get back to you.</p>
  <div class="field"></div><div class="field"></div><div class="field"></div>
  <span class="btn btn-orange">Send »</span>
</section>

<section class="quote abs">
  <div class="quote-circle abs">“The best weight loss experience of my life”<small>Carla B.</small></div>
  <div class="photo abs" role="img" aria-label="Smiling retreat guest outdoors"></div>
</section>

<section class="real abs">
  <h3>Real People – Real Results</h3>
  <div class="row">
    <div class="photo" role="img" aria-label="Guests celebrating their progress"></div>
    <ul><li>100% of guests lose weight</li><li>Lose up to 6kg in one week</li><li>Normal people just like you</li><li>Read testimonials</li></ul>
  </div>
</section>

<section class="results abs">
  <h3>Results Our Clients Have Achieved</h3>
  <div class="cols">
    <ul><li>Weight loss</li><li>Centimetre loss</li><li>Improved fitness</li><li>Lower blood pressure</li></ul>
    <ul><li>Improved mobility and agility</li><li>Healthier eating habits</li><li>Better sleep and energy</li><li>Lasting confidence</li></ul>
    <ul><li>Stronger muscles</li><li>Reduced stress levels</li><li>New friendships</li><li>Support after you leave</li></ul>
  </div>
</section>

<footer class="site-footer abs">
  <div class="fcol"><h4>The Best Programs</h4><ul><li>Weight Loss Retreat</li><li>Renowned Boot Camp</li><li>Fitness Camp</li><li>At home program</li><li>Local groups</li></ul></div>
  <div class="fcol"><h4>The best Locations</h4><ul><li>Blue Mountains</li><li>Sunshine Coast</li><li>Hunter Valley</li><li>Local programs</li></ul></div>
  <div class="fcol"><h4>About Us</h4><ul><li>Why PineLoop</li><li>Our Expert Team</li><li>Our Research</li><li>Careers</li><li>Contact</li></ul></div>
  <div class="fcol"><h4>Results for...</h4><ul><li>Weight loss</li><li>Fitness</li><li>Healthy eating</li><li>Lifestyle change</li></ul></div>
  <div class="fcol"><h4>FREE Information</h4><ul><li>Request a brochure</li><li>Ask a question</li><li>Newsletter</li></ul></div>
</footer>
<div class="footer-bar abs"><span>Contact Us | Book Now | Privacy</span><span>© PineLoop Wellbeing Pty Ltd</span></div>

</body>
</html>
```